Hypnotherapy- past life regression-life between lives therapist needs a website

I need a website that is enticing and spiritual in its feeling. It needs to have a lot of beautiful nature pictures included. The theme is "Willowmere Hollow- what could you uncover....Tides Lanterns Compass"
Because all of us have the answers to living our best life, they are in our subconcious. But not everyone is capable of accessing them. Hypnosis accesses the subconcious and helps to create new neural pathways in the brain which can create new behaviors and responses to situations.
Hypnosis can help with anxiety, pain relief, weight loss, smoking/vaping cessation, self confidence......anything about yourself that you want to change.
Exploration of past lives and life between lives can reveal things related to ones current life. For example, perhaps your fear of deep water is a result of drowning in a past life. Once this has been discovered, it can lead to changes in ones current life.
Almost any personal behavior one wants to change, can be helped through hypnotherapy.
I need a page for testimonials, a place for scheduling (I will have a link to my scheduling app) some information about hypnotherapy.
I am uploading my logo files. My business card will be using the black and gold style, but my website does not have to reflect that. It can be based on the caramel and deep green like full color logo. Earthy, calm colors.
I also like the mock up of my logo on the beach and there was one on a starry night sky that I also liked.
Target Market(s)
men and women ages 25-50
Industry/Entity Type
natural health and wellness, spirituality
Number of Pages Required
4 page
Requirements
Must have
- a page for testimonials, perhaps with a beautiful nature picture with each one, I will have approximately 6. A link to schedule a complimentary intro session, preferably on the first page
Should not have
- no swinging watches or other sterotyped hypnosis symbols

```html
<!DOCTYPE html>
<html lang="en">
<head>
<meta charset="utf-8">
<title>Willowmere Hollow – Hypnotherapy</title>
<link href="https://fonts.googleapis.com/css2?family=Lora:wght@400;500;600&family=Open+Sans:wght@400;600&display=swap" rel="stylesheet">
<style>
:root{
  --olive:#6c6c42;
  --olive-dark:#5e5e38;
  --sage:#d4d5c7;
  --caramel:#e9a053;
  --ink:#2a2a2a;
  --muted:#6f6f6f;
  --white:#ffffff;
  --sand:#c8b283;
}
*{box-sizing:border-box;margin:0;padding:0}
html,body{width:1200px;height:5071px;overflow:hidden}
body{position:relative;font-family:"Open Sans",Arial,sans-serif;color:var(--ink);background:var(--white)}
.abs{position:absolute}
section,header,footer,.topbar{position:absolute;left:0;width:1200px;overflow:hidden}
.btn{position:absolute;display:flex;align-items:center;justify-content:center;background:var(--caramel);color:#fff;border-radius:30px;font-family:"Lora",Georgia,serif;font-size:14px;letter-spacing:1.2px;text-transform:uppercase;box-shadow:0 6px 14px rgba(233,160,83,.35)}
.eyebrow{position:absolute;font-size:13px;letter-spacing:1px;color:var(--caramel);text-transform:uppercase;padding-left:40px}
.eyebrow::before{content:"";position:absolute;left:0;top:50%;width:28px;height:1px;background:var(--caramel)}
.h2{position:absolute;font-family:"Lora",Georgia,serif;font-size:31px;font-weight:400;color:var(--ink)}

.topbar{top:0;height:40px;background:var(--olive);color:#fff;font-size:14px}
.topbar span{position:absolute;top:11px;display:flex;align-items:center;gap:8px}

.site-header{top:40px;height:98px;background:#fff}
.brand{position:absolute;left:40px;top:30px;display:flex;align-items:center;gap:8px;font-family:"Lora",Georgia,serif;font-size:14px;font-weight:600;color:var(--caramel);text-transform:uppercase;letter-spacing:.5px}
.brand i{width:28px;height:28px;border-radius:50%;background:var(--caramel);display:block}
.nav a{position:absolute;top:40px;font-family:"Lora",Georgia,serif;font-size:12.5px;letter-spacing:.8px;color:var(--ink);text-decoration:none;text-transform:uppercase}

.hero{top:138px;height:641px}
.hero-bg{position:absolute;inset:0;background:radial-gradient(ellipse at 65% 55%,#d9c597 0%,#c6ae7e 45%,#a9925f 100%)}
.hero h1{position:absolute;top:140px;width:100%;text-align:center;font-family:"Lora",Georgia,serif;font-weight:400;font-size:40px;line-height:58px;color:#fff}
.hero p{position:absolute;left:250px;width:700px;top:286px;text-align:center;font-size:14px;line-height:28px;color:#fff}

.about{top:779px;height:716px}
.about-photo{position:absolute;left:119px;top:139px;width:427px;height:427px;border-radius:50%;background:linear-gradient(180deg,#7ea9d6 0%,#c8d9ea 45%,#9a9a98 70%,#6f6f6d 100%)}
.about p.lead{position:absolute;left:642px;top:208px;width:480px;font-size:14px;line-height:29px;color:#444}
.feature{position:absolute;width:240px;height:50px}
.feature .ic{position:absolute;left:0;top:2px;width:46px;height:46px;border-radius:50%;background:#7e7e5e}
.feature b{position:absolute;left:66px;top:2px;font-family:"Lora",Georgia,serif;font-weight:400;font-size:15px;white-space:nowrap}
.feature small{position:absolute;left:66px;top:28px;font-size:12px;color:#9a9a9a;white-space:nowrap}

.services{top:1495px;height:1031px;background:var(--sage)}
.card{position:absolute;width:306px;background:#fff;border-radius:6px;text-align:center}
.card .ph{position:absolute;left:10px;right:10px;top:10px;height:190px}
.card h3{position:absolute;left:0;right:0;top:232px;font-family:"Lora",Georgia,serif;font-weight:500;font-size:25px}
.card p{position:absolute;left:20px;right:20px;top:280px;font-size:14px;line-height:28px;color:#444}

.why{top:2526px;height:736px}
.video{position:absolute;left:65px;top:218px;width:488px;height:302px;border-radius:20px;background:radial-gradient(circle at 58% 45%,#6d6a5e 0%,#2c2b22 45%,#15150f 100%);box-shadow:0 10px 24px rgba(0,0,0,.18)}
.play{position:absolute;left:216px;top:124px;width:56px;height:56px;border-radius:50%;background:var(--caramel)}
.why p.lead{position:absolute;left:609px;top:254px;width:505px;font-size:14px;line-height:28px;color:#444}
.why ul{list-style:none}
.why li{position:absolute;font-family:"Lora",Georgia,serif;font-size:13.5px;letter-spacing:.4px;color:#333;padding-left:26px}
.why li::before{content:"";position:absolute;left:0;top:2px;width:13px;height:13px;border:1.5px solid var(--caramel);border-radius:50%}

.testimonials{top:3262px;height:570px;background:var(--olive)}
.testimonials .eyebrow{color:#fff}
.testimonials .eyebrow::before{background:#fff}
.quote{position:absolute;top:282px;font-family:"Lora",Georgia,serif;font-size:14px;line-height:28px;color:#fff;white-space:nowrap}
.quote-name{position:absolute;top:394px;font-family:"Lora",Georgia,serif;font-weight:600;font-size:15px;line-height:20px;color:#fff}
.quote-name small{display:block;font-size:10px;font-weight:400;opacity:.55}
.avatar{position:absolute;border-radius:50%;border:4px solid #fff;background:linear-gradient(160deg,#cdb8a4,#8f7a6a)}

.appointment{top:3832px;height:783px}
.agent{position:absolute;left:60px;top:68px;width:505px;height:715px;background:linear-gradient(180deg,#f4efe9 0%,#e3d7cc 40%,#2f3449 70%,#23273a 100%)}
.form{position:absolute;left:600px;top:288px;width:535px;height:378px;background:var(--olive)}
.field{position:absolute;left:47px;width:441px;background:#fff;border:1px solid #ccc;font-size:11px;color:#999;padding:8px 14px}

.site-footer{top:4615px;height:456px;background:var(--olive);color:#fff}
.site-footer .brand{left:82px;top:145px;color:var(--caramel)}
.social{position:absolute;top:240px;width:30px;height:30px;border-radius:50%;border:1px solid rgba(255,255,255,.6)}
.fcol h4{position:absolute;top:112px;font-family:"Lora",Georgia,serif;font-weight:500;font-size:17px;padding-left:40px}
.fcol h4::before{content:"";position:absolute;left:0;top:50%;width:28px;height:1px;background:#fff}
.fcol a{position:absolute;font-size:13px;color:#fff;text-decoration:none}
.copy{position:absolute;left:0;top:428px;width:100%;text-align:center;font-size:11px;color:rgba(255,255,255,.8)}
</style>
</head>
<body>

<div class="topbar">
  <span style="left:64px"><svg width="12" height="12" viewBox="0 0 24 24" fill="none" stroke="#e9a053" stroke-width="2"><path d="M22 16.9v3a2 2 0 0 1-2.2 2A19.8 19.8 0 0 1 2.1 4.2 2 2 0 0 1 4.1 2h3a2 2 0 0 1 2 1.7c.1 1 .4 1.9.7 2.8a2 2 0 0 1-.5 2.1L8 9.9a16 16 0 0 0 6 6l1.3-1.3a2 2 0 0 1 2.1-.4c.9.3 1.8.6 2.8.7a2 2 0 0 1 1.7 2z"/></svg>555-014-2298</span>
  <span style="left:198px"><svg width="12" height="10" viewBox="0 0 24 18" fill="none" stroke="#e9a053" stroke-width="2"><rect x="1" y="1" width="22" height="16"/><path d="M1 1l11 9 11-9"/></svg>hello@willowmerehollow.com</span>
</div>

<header class="site-header">
  <div class="brand"><i></i>Willowmere Hollow</div>
  <nav class="nav">
    <a style="left:437px">Home</a>
    <a style="left:507px">About</a>
    <a style="left:582px">Services</a>
    <a style="left:675px">Testimonials</a>
    <a style="left:803px">FAQs</a>
    <a style="left:866px">Contact</a>
  </nav>
  <div class="btn" style="left:1018px;top:28px;width:152px;height:46px;font-size:12.5px">Book Online</div>
</header>

<section class="hero">
  <div class="hero-bg" role="img" aria-label="Stone archway standing alone in misty golden desert dunes"></div>
  <h1>Willowmere Hollow<br>what could you uncover</h1>
  <p>Exploration of past lives and life between lives can reveal things related to ones current life. For example, perhaps your fear of deep water is a result of drowning in a past life. Once this has been discovered, it can lead to changes in ones current life.</p>
  <div class="btn" style="left:510px;top:405px;width:178px;height:47px">Book Online</div>
</section>

<section class="about">
  <div class="about-photo" role="img" aria-label="Man climbing a stone staircase toward a cloudy blue sky"></div>
  <div class="eyebrow" style="left:642px;top:115px">Who We Are</div>
  <div class="h2" style="left:642px;top:143px">About Us</div>
  <p class="lead">Etiam scelerisque nec elit ac efficitur. Duis vestibulum magna sit amet ante gravida malesuada. Nunc gravida dui scelerisque libero venenatis hendrerit vestibulum euismod, lacus.</p>
  <div class="feature" style="left:642px;top:331px"><span class="ic"></span><b>Qualified Therapies</b><small>45 years of experience</small></div>
  <div class="feature" style="left:884px;top:331px"><span class="ic"></span><b>Individual Counseling</b><small>Mental help for families</small></div>
  <div class="feature" style="left:642px;top:418px"><span class="ic"></span><b>Couples Counseling</b><small>45 years of experience</small></div>
  <div class="feature" style="left:884px;top:418px"><span class="ic"></span><b>Referring Therapists</b><small>Experts you can trust</small></div>
  <div class="btn" style="left:642px;top:524px;width:170px;height:49px">Learn More</div>
</section>

<section class="services">
  <div class="eyebrow" style="left:122px;top:107px">What We Do</div>
  <div class="h2" style="left:122px;top:135px">Popular Services</div>
  <div class="btn" style="left:778px;top:118px;width:280px;height:47px">Explore More Services</div>

  <div class="card" style="left:112px;top:256px;height:357px"><div class="ph" role="img" aria-label="Anxious woman holding her head on a sofa" style="background:linear-gradient(135deg,#c9c3bb,#8c8177)"></div><h3>Anxiety</h3><p>Lorem ipsum dolor sit amet consectetur adipiscing.</p></div>
  <div class="card" style="left:437px;top:256px;height:357px"><div class="ph" role="img" aria-label="Woman at a laptop holding her aching back" style="background:linear-gradient(135deg,#ede7df,#b9ada0)"></div><h3>Pain Relief</h3><p>Lorem ipsum dolor sit amet consectetur adipiscing.</p></div>
  <div class="card" style="left:763px;top:256px;height:357px"><div class="ph" role="img" aria-label="Slim waist with a tape measure and a green apple" style="background:linear-gradient(135deg,#e9e9e7,#8f9c5a)"></div><h3>Weight Loss</h3><p>Lorem ipsum dolor sit amet consectetur adipiscing.</p></div>

  <div class="card" style="left:112px;top:633px;height:350px"><div class="ph" role="img" aria-label="Hands breaking a cigarette in half" style="background:linear-gradient(135deg,#5c5c5c,#c49a80)"></div><h3>Smoking Cessation</h3><p>Lorem ipsum dolor sit amet consectetur adipiscing.</p></div>
  <div class="card" style="left:437px;top:633px;height:350px"><div class="ph" role="img" aria-label="Man with open arms on a misty mountain top" style="background:linear-gradient(180deg,#dcdcda,#8a857c)"></div><h3>Self Confidence</h3><p>Lorem ipsum dolor sit amet consectetur adipiscing.</p></div>
  <div class="card" style="left:763px;top:633px;height:350px"><div class="ph" role="img" aria-label="Couple sitting back to back on a sofa after an argument" style="background:linear-gradient(135deg,#e6ded3,#3a5a8c)"></div><h3>Relation Issue</h3><p>Lorem ipsum dolor sit amet consectetur adipiscing.</p></div>
</section>

<section class="why">
  <div class="video" role="img" aria-label="Open door glowing with light in a dark room, video preview"><span class="play"></span><svg class="abs" style="left:232px;top:140px" width="24" height="24" viewBox="0 0 24 24" fill="none" stroke="#fff" stroke-width="1.5"><circle cx="12" cy="12" r="9"/><path d="M10 8l6 4-6 4z"/></svg></div>
  <div class="eyebrow" style="left:609px;top:163px">Why We Are</div>
  <div class="h2" style="left:609px;top:210px;color:#777">Why Hypnosis Therapy?</div>
  <p class="lead" style="top:253px">Mauris cursus posuere sem non fermentum donec condime ntum, nibh ut viverra molestie, urna dui convallis tortor, sed dignissim arcu ex sed</p>
  <ul>
    <li style="left:609px;top:343px">Bipolar Disorders</li>
    <li style="left:866px;top:343px">Relationship Therapy</li>
    <li style="left:609px;top:383px">Anxiety Therapy</li>
    <li style="left:866px;top:383px">Family Therapy</li>
    <li style="left:609px;top:423px">Stress Management</li>
    <li style="left:866px;top:423px">Curing Addictions</li>
    <li style="left:609px;top:463px">Executive Coaching</li>
    <li style="left:866px;top:463px">Emergency Services</li>
    <li style="left:609px;top:503px">Depression Therapy</li>
    <li style="left:866px;top:503px">Brief Therapy</li>
  </ul>
  <div class="btn" style="left:609px;top:558px;width:159px;height:46px">Read More</div>
</section>

<section class="testimonials">
  <div class="eyebrow" style="left:75px;top:153px">Testimonials</div>
  <div class="h2" style="left:75px;top:182px;color:#fff">Our Happy Clients</div>

  <div class="quote" style="left:75px">Nam arcu sit amet erat accumsan vehicula.<br>Nunc sapien in posuere volutpat. Sed elit<br>accumsan enim malesuada eu.</div>
  <div class="quote-name" style="left:75px">Thornbury<small>Client</small></div>

  <div class="quote" style="left:478px">Cras vestibulum<br>Curabitur aliquet<br>sapien non arcu.</div>
  <div class="avatar" style="left:478px;top:380px;width:64px;height:64px"></div>
  <div class="quote-name" style="left:556px">Wren<small>Client</small></div>

  <svg class="abs" style="left:690px;top:0" width="510" height="570" viewBox="0 0 510 570">
    <path d="M120 570 C30 420 60 110 230 0 L510 0 L510 570 Z" fill="#e79a59"/>
    <path d="M160 570 C80 420 110 130 300 0 L510 0 L510 570 Z" fill="#b89a82" role="img" aria-label="Women embracing warmly at a support group"/>
  </svg>
  <div class="avatar" style="left:638px;top:105px;width:74px;height:74px"></div>
  <div class="avatar" style="left:610px;top:250px;width:74px;height:74px"></div>
  <div class="avatar" style="left:627px;top:395px;width:76px;height:76px"></div>
</section>

<section class="appointment">
  <div class="agent" role="img" aria-label="Smiling support agent wearing a headset"></div>
  <div class="eyebrow" style="left:600px;top:200px">Who We Are</div>
  <div class="h2" style="left:600px;top:228px">Book An Appointment Now</div>
  <div class="form">
    <div class="field" style="top:48px;height:36px">Name</div>
    <div class="field" style="top:94px;height:36px">Email</div>
    <div class="field" style="top:138px;height:82px">Message</div>
    <div class="btn" style="left:47px;top:233px;width:441px;height:47px;box-shadow:none">Send</div>
  </div>
</section>

<footer class="site-footer">
  <div class="brand"><i></i>Willowmere Hollow</div>
  <span class="social" style="left:80px"></span>
  <span class="social" style="left:126px"></span>
  <span class="social" style="left:172px"></span>
  <span class="social" style="left:218px"></span>
  <div class="fcol">
    <h4 style="left:342px">Links</h4>
    <a style="left:342px;top:167px">Home</a>
    <a style="left:342px;top:205px">About</a>
    <a style="left:342px;top:243px">Services</a>
    <a style="left:342px;top:281px">Contact</a>
  </div>
  <div class="fcol">
    <h4 style="left:556px">Benefits</h4>
    <a style="left:556px;top:167px">Weight Lose</a>
    <a style="left:556px;top:205px">Pain Relief</a>
    <a style="left:556px;top:243px">Self Confidence</a>
  </div>
  <div class="fcol">
    <h4 style="left:772px">Contact Us</h4>
    <a style="left:802px;top:167px">Larchfield Vic 3290</a>
    <a style="left:802px;top:209px">hello@willowmerehollow.com</a>
    <a style="left:802px;top:251px">555-014-2298</a>
    <svg class="abs" style="left:772px;top:170px" width="12" height="14" viewBox="0 0 24 28" fill="none" stroke="#fff" stroke-width="2"><path d="M12 27s10-9 10-16a10 10 0 0 0-20 0c0 7 10 16 10 16z"/><circle cx="12" cy="11" r="3"/></svg>
    <svg class="abs" style="left:772px;top:213px" width="13" height="10" viewBox="0 0 24 18" fill="none" stroke="#fff" stroke-width="2"><rect x="1" y="1" width="22" height="16"/><path d="M1 1l11 9 11-9"/></svg>
    <svg class="abs" style="left:772px;top:253px" width="12" height="12" viewBox="0 0 24 24" fill="none" stroke="#fff" stroke-width="2"><path d="M22 16.9v3a2 2 0 0 1-2.2 2A19.8 19.8 0 0 1 2.1 4.2 2 2 0 0 1 4.1 2h3a2 2 0 0 1 2 1.7c.1 1 .4 1.9.7 2.8a2 2 0 0 1-.5 2.1L8 9.9a16 16 0 0 0 6 6l1.3-1.3a2 2 0 0 1 2.1-.4c.9.3 1.8.6 2.8.7a2 2 0 0 1 1.7 2z"/></svg>
  </div>
  <div class="copy">© 2023 Willowmere Hollow. All Rights Reserved.</div>
</footer>

</body>
</html>
```